High end Electrical/home automation Business Card

Need a card for a high end electrical and home automation company utilising the existing logo.
Phone
Email
Website

Like black look with raised detail. Don’t necessarily need to keep colour of logo it could be made grayscale or white etc

Target Market(s)

High end clients

Contact Information for Business Card

Ridgeline Electrical

Requirements
Must have
• Logo, phone, email, website, address

High end look
Nice to have
• Black background card
Raised font
Should not have
• Lots of colour

```html
<!DOCTYPE html>
<html lang="en">
<head>
<meta charset="utf-8">
<title>Ridgeline Electrical – Business Card</title>
<link rel="stylesheet" href="https://fonts.googleapis.com/css2?family=Roboto+Condensed:wght@400;700&family=Roboto:wght@400&display=swap">
<style>
  :root {
    --page: #ffffff;
    --bleed: #a7a7a7;
    --card-black: #000000;
    --card-white: #ffffff;
    --mark-grey: #3d3d3d;
    --ink-dark: #111111;
    --ink-mid: #6b6b6b;
    --icon-bg: #d4d4d4;
    --icon-fg: #ffffff;
    --social: #c4c4c4;
    --label: #000000;
  }
  * { margin: 0; padding: 0; box-sizing: border-box; }
  html, body {
    width: 1200px; height: 1200px; overflow: hidden;
    background: var(--page);
    font-family: "Roboto Condensed", Arial, sans-serif;
  }
  .canvas { position: relative; width: 1200px; height: 1200px; }

  .bleed-frame { position: absolute; background: var(--bleed); }
  .card-front-frame { left: 150px; top: 156px; width: 562px; height: 338px; }
  .card-back-frame { left: 552px; top: 767px; width: 563px; height: 337px; }

  .trim-area {
    position: absolute; left: 18px; top: 18px;
    width: 527px; height: 300px; overflow: hidden;
    background: var(--card-black);
  }
  .card-back-frame .trim-area { background: var(--card-white); top: 18px; left: 19px; }

  .bleed-label {
    position: absolute; font-family: "Roboto", Arial, sans-serif;
    font-size: 11px; color: var(--label); line-height: 1;
  }
  .bleed-label.bottom { left: 50%; bottom: 1px; transform: translateX(-50%); }
  .bleed-label.side { left: 3px; top: 50%; transform: translate(-14px, -50%) rotate(90deg); transform-origin: center; left: 4px; }

  .brand-lockup { position: absolute; text-align: center; color: var(--mark-grey); }
  .brand-dot { display: block; margin: 0 auto; border-radius: 50%; background: var(--mark-grey); }
  .brand-name { display: block; font-weight: 700; letter-spacing: -0.3px; white-space: nowrap; }
  .brand-url { display: block; white-space: nowrap; letter-spacing: 2px; }

  .front-lockup { left: 0; width: 527px; top: 94px; }
  .front-lockup .brand-dot { width: 60px; height: 60px; margin-bottom: 22px; }
  .front-lockup .brand-name { font-size: 26px; line-height: 28px; }
  .front-lockup .brand-url { font-size: 14px; line-height: 18px; }

  .back-panel { position: absolute; left: 0; top: 0; width: 527px; height: 300px; }

  .back-lockup { left: 0; width: 238px; top: 78px; }
  .back-lockup .brand-dot { width: 44px; height: 44px; margin-bottom: 14px; }
  .back-lockup .brand-name { font-size: 19px; line-height: 21px; }
  .back-lockup .brand-url { font-size: 10px; line-height: 14px; letter-spacing: 1.5px; }

  .person { position: absolute; right: 25px; top: 38px; text-align: right; }
  .person-name { font-size: 25px; font-weight: 700; color: var(--ink-dark); line-height: 28px; }
  .person-title { font-size: 14px; color: var(--ink-mid); letter-spacing: 0.5px; line-height: 18px; }
  .title-rule { width: 46px; height: 3px; background: var(--ink-mid); margin: 6px 0 0 auto; }

  .contact-list { position: absolute; right: 25px; top: 114px; list-style: none; }
  .contact-item {
    display: flex; align-items: center; justify-content: flex-end;
    color: var(--ink-mid); font-size: 15px; line-height: 21px;
    margin-bottom: 10px; text-align: right;
  }
  .contact-item .icon { flex: none; width: 26px; height: 26px; margin-left: 10px; }

  .social-row { position: absolute; left: 221px; top: 257px; display: flex; gap: 8px; }
  .social-chip { width: 22px; height: 22px; background: var(--social); }
</style>
</head>
<body>
<div class="canvas">

  <section class="bleed-frame card-front-frame" aria-label="Card front">
    <div class="trim-area">
      <div class="brand-lockup front-lockup">
        <span class="brand-dot"></span>
        <span class="brand-name">Ridgeline Electrical</span>
        <span class="brand-url">www.ridgelineelectrical.com</span>
      </div>
    </div>
    <span class="bleed-label side">bleed</span>
    <span class="bleed-label bottom">bleed</span>
  </section>

  <section class="bleed-frame card-back-frame" aria-label="Card back">
    <div class="trim-area">
      <svg class="back-panel" viewBox="0 0 527 300" width="527" height="300" aria-hidden="true">
        <polygon points="0,0 301,0 169,300 0,300" fill="var(--card-black)"/>
      </svg>

      <div class="brand-lockup back-lockup">
        <span class="brand-dot"></span>
        <span class="brand-name">Ridgeline Electrical</span>
        <span class="brand-url">www.ridgelineelectrical.com</span>
      </div>

      <div class="person">
        <p class="person-name">Martin Cole</p>
        <p class="person-title">CORPORATE MANAGER</p>
        <div class="title-rule"></div>
      </div>

      <ul class="contact-list">
        <li class="contact-item">
          <span>1.603.555.0142</span>
          <svg class="icon" viewBox="0 0 26 26" aria-hidden="true">
            <circle cx="13" cy="13" r="13" fill="var(--icon-bg)"/>
            <path d="M7 10c0-2 2-3 6-3s6 1 6 3v1h-3v-1.5h-6V11H7z M8.5 12h9l1 6h-11z" fill="var(--icon-fg)"/>
          </svg>
        </li>
        <li class="contact-item">
          <span>480 Harbor Mill Road<br>Concord, NH 03301</span>
          <svg class="icon" viewBox="0 0 26 26" aria-hidden="true">
            <circle cx="13" cy="13" r="13" fill="var(--icon-bg)"/>
            <path d="M13 6l7 6h-2v7h-3.5v-4h-3v4H8v-7H6z" fill="var(--icon-fg)"/>
          </svg>
        </li>
        <li class="contact-item">
          <span>martincole@ridgelineelectrical.com</span>
          <svg class="icon" viewBox="0 0 26 26" aria-hidden="true">
            <circle cx="13" cy="13" r="13" fill="var(--icon-bg)"/>
            <rect x="7" y="9" width="12" height="9" fill="var(--icon-fg)"/>
            <path d="M7 9l6 5 6-5" fill="none" stroke="var(--icon-bg)" stroke-width="1.2"/>
          </svg>
        </li>
      </ul>

      <div class="social-row" aria-label="Social profiles">
        <span class="social-chip"></span>
        <span class="social-chip"></span>
        <span class="social-chip"></span>
      </div>
    </div>
    <span class="bleed-label side">bleed</span>
    <span class="bleed-label bottom">bleed</span>
  </section>

</div>
</body>
</html>
```